依頼詳細
【カラー】
・今のサイトのロゴやフォントに使用されているえんじ色は使用しなくて構いませ
ん。むしろ使用しないでください。
・薄いベージュや藍色をどこかに入れられたら入れてください。
必須ではないので入れなくても構いません。

【要素】
①グローバルナビ
・お知らせ
・ごあいさつ
・診療案内
・乳がん検診
・施設案内
・ご予約
・アクセスマップ
・よくある質問
・リンク

③トップコンテンツ
・お知らせ(ダミーテキストで構いません)
・ごあいさつ(ダミーテキストで構いません)
・診療案内(ダミーテキストで構いません)
┗診療時間/診療内容
診療内容の下層ページへ飛ぶリンク(ボタンなど)を貼ってください。
・乳がん検診(ダミーテキストで構いません)
乳がん検診の下層ページへ飛ぶリンク(ボタンなど)を貼ってください。
・施設案内(ダミーテキストで構いません)
施設案内の写真を表示
※のちに変更がありますが、とりあえず現状の施設の写真(下記URLより)を使って ください。
http://www.yurune-clinic.net/contents/shisetsu.htm
・アクセスマップ(ダミーテキストで構いません)
・よくある質問(ダミーテキストで構いません)
・リンク(ダミーテキストで構いません)
※使用する画像デザインはすべてお任せします。
※ご予約について
電話からのお問い合わせが多いので、スマホ利用時はそこから
電話ができる用にします。PC・スマホ共々、場所はご予約がしやすい所
でお願いします。お任せします。
サイトURL
http://www.yurune-clinic.net/
ページ数
2ページ
希望イメージ
• +5 0 +5
• シンプル
複雑
• 単色
カラフル
• 暗い
明るい
• 日常
高級
• 遊び心
厳粛
• 未来的
伝統的
• 女性的
男性的
希望する色
藍色、または薄いベージュ系の色を使用できそうなら使用してください。必ずではございません。
納品ファイル
• 高解像度JPG (.jpg)
• フォトショップ形式 (.psd)
補足説明
今回のコンペで当選された方には、中ページ(PC・スマホ)のデザイン制作を追加でお願いする可能性がございます。
報酬金額2万円程度を想定しておりますので、その際はお力添えお願いいたします。
依頼公開後の追記内容
現時点で、実質3案のご提案のみとなっており提案数に不安があるため、締め切り日を変更させていただきます。
現在いただいているご提案を拝見して、気になった点を下記にまとめておりますので今後ご提案いただける方はそちらもご留意いただけますと幸いです。
●あまり主張の強すぎる背景柄は避けたい
●ハイクオリティなイメージを喚起するため、極力すっきりとしたフォントが望ましい
(あまり丸みを帯びすぎていないもの等)
●フラットデザインのようなシンプルかつ洗練されたイメージが望ましい

ざっくりとした要望となってしまいますが、皆様のお力添えをいただければと思います。
引き続きよろしくお願いします。

病院系のサイトにはない新しいデザインと、小鳥という動物モチーフながら
動物病院のようにもならず、女性向けにきれいにまとまったデザインでした
pika-lune様のデザインを当選とさせていただきます。

この度は弊社デザインコンペへご提案いただき、誠にありがとうございました。
当選までに時間がかかり、皆様をお待たせしてしまいましたこと、お詫び申し上げます。
今回は、病院でありながら、病院らしくないサイトという無茶な依頼にも関わらず素敵なデザインが多く、とても参考になりました。
今後とも、弊社にお力添えいただけますと幸いです。
有難うございました。

```html
<!DOCTYPE html>
<html lang="ja">
<head>
<meta charset="utf-8">
<title>ゆるね乳腺クリニック</title>
<link rel="stylesheet" href="https://fonts.googleapis.com/css2?family=Noto+Sans+JP:wght@400;500;700&family=Noto+Serif+JP:wght@500&family=Cormorant+Garamond:ital@1&display=swap">
<style>
:root{
  --navy:#1f3a6b;
  --navy-dark:#172c52;
  --sky:#a9cde8;
  --sky-light:#dcecf7;
  --beige:#f4ede1;
  --beige-deep:#ebe0cc;
  --ink:#333;
  --muted:#777;
  --line:#c9ced8;
  --white:#fff;
}
*{margin:0;padding:0;box-sizing:border-box}
html,body{width:1200px;height:4272px;overflow:hidden}
body{position:relative;background:var(--white);font-family:"Noto Sans JP",sans-serif;color:var(--ink);font-size:13px;line-height:1.8}
.abs{position:absolute}
a{color:inherit;text-decoration:none}

.backdrop{position:absolute;left:0;top:0;width:1200px;height:4272px}

.hero{left:0;top:0;width:1200px;height:600px;background:linear-gradient(180deg,#7fb2dc 0%,var(--sky) 45%,var(--sky-light) 80%,#fff 100%)}
.brand{left:0;top:318px;width:1200px;text-align:center;color:var(--white)}
.brand-name{font-family:"Noto Serif JP",serif;font-weight:500;font-size:40px;letter-spacing:.08em;line-height:1.3}
.brand-en{font-family:"Cormorant Garamond",serif;font-style:italic;font-size:16px;letter-spacing:.1em}

.gnav{left:1000px;top:22px;width:160px}
.gnav li{list-style:none;font-size:13px;color:var(--white);line-height:26px;padding-left:4px}
.gnav .reserve{margin-top:12px;background:var(--navy);text-align:center;line-height:34px;font-weight:500}

.sec-title{font-size:20px;font-weight:500;letter-spacing:.15em;text-align:center;color:var(--ink)}
.sec-title::after{content:"";display:block;width:40px;height:2px;background:var(--navy);margin:10px auto 0}
.sub-label{display:inline-block;border:1px solid var(--navy);color:var(--navy);font-size:12px;padding:0 18px;line-height:26px;background:#fff}

.news-label{left:180px;top:690px;font-size:20px;font-weight:500;letter-spacing:.15em}
.news-label::after{content:"";display:block;width:30px;height:2px;background:var(--navy);margin-top:8px}
.news{left:360px;top:680px;width:640px}
.news li{list-style:none;display:flex;gap:24px;border-bottom:1px dotted var(--line);line-height:32px;font-size:13px}
.news time{color:var(--navy);width:120px}
.news-more{left:860px;top:858px;font-size:12px;color:var(--navy)}

.card{left:160px;top:900px;width:880px;height:640px;background:var(--white);box-shadow:0 2px 14px rgba(0,0,0,.08)}
.doctor{left:80px;top:120px;width:240px;height:220px;background:linear-gradient(135deg,#e7ecf1,#c9d3dc)}
.doctor-cap{left:80px;top:348px;width:240px;text-align:center;font-size:11px;color:var(--muted)}
.profile{left:360px;top:120px;width:460px;font-size:12px;line-height:1.9}
.profile h4{font-size:13px;color:var(--navy);font-weight:700;margin-bottom:2px}
.profile p+h4{margin-top:14px}
.greet-btn{left:0;top:402px;width:880px;text-align:center}
.greet-text{left:80px;top:450px;width:720px;font-size:12px;line-height:2}

.hours-label{left:200px;top:1660px}
.hours{left:160px;top:1705px;width:420px;border-collapse:collapse;font-size:11px;background:#fff}
.hours th,.hours td{border:1px solid var(--line);text-align:center;height:28px}
.hours th:first-child,.hours td:first-child{width:126px}
.hours thead th{background:var(--beige)}
.hours-note{left:160px;top:1800px;font-size:10px;color:var(--muted);line-height:1.6}
.menu-label{left:620px;top:1660px}
.menus{left:600px;top:1712px;width:460px;display:flex;justify-content:space-between}
.menu{width:104px;height:104px;border:1px solid var(--navy);border-radius:50%;display:flex;align-items:center;justify-content:center;text-align:center;font-size:11px;line-height:1.5;background:#fff}
.btn{display:inline-block;background:var(--navy);color:#fff;font-size:12px;text-align:center;line-height:36px;padding:0 30px}
.btn::after{content:" ›"}
.menu-btn{left:700px;top:1850px}

.screen{left:0;top:2020px;width:1200px;height:220px;background:var(--white)}
.screen-text{left:240px;top:88px;width:720px;text-align:center;font-size:12px;line-height:1.9}
.screen-btn{left:0;top:160px;width:1200px;text-align:center}

.facility{left:0;top:2300px;width:1200px;height:680px;background:linear-gradient(180deg,#eef1f4,#f7f8fa)}
.fac-main{left:160px;top:120px;width:880px;height:380px;background:linear-gradient(120deg,#f6f7f8 0%,#dde3e8 60%,#c6ced6 100%)}
.fac-cap{left:170px;top:470px;font-size:11px;color:var(--ink)}
.thumbs{left:160px;top:520px;width:880px;display:flex;gap:8px}
.thumbs div{flex:1;height:80px;background:linear-gradient(135deg,#dfe4e9,#b7c1cb)}

.faq{left:160px;top:3080px;width:880px}
.faq li{list-style:none;display:flex;align-items:center;height:32px;border-bottom:1px solid var(--line);font-size:12px}
.faq .q{width:22px;height:22px;background:var(--navy);color:#fff;font-size:11px;text-align:center;line-height:22px;margin-right:14px}
.faq .chev{margin-left:auto;color:var(--navy);font-size:14px;padding-right:8px}
.faq-btn{left:0;top:3418px;width:1200px;text-align:center}

.acc-name{left:180px;top:3720px;font-family:"Noto Serif JP",serif;font-size:24px;color:var(--navy);letter-spacing:.05em}
.acc-addr{left:180px;top:3770px;font-size:11px;color:var(--muted);line-height:1.7}
.acc-tel{left:180px;top:3910px;font-size:34px;font-weight:500;color:var(--navy);display:flex;align-items:center;gap:10px}
.map{left:660px;top:3620px;width:380px;height:320px;background:linear-gradient(135deg,#d8d8d8,#bdbdbd)}

.links{left:160px;top:4080px;width:880px;display:grid;grid-template-columns:repeat(4,1fr);font-size:11px;line-height:2}
.links a::before{content:"› ";color:var(--navy)}
.footer{left:0;top:4240px;width:1200px;height:32px;background:var(--navy-dark);color:#fff;font-size:10px;text-align:center;line-height:32px}
</style>
</head>
<body>

<svg class="backdrop" viewBox="0 0 1200 4272" aria-hidden="true">
  <rect x="0" y="560" width="1200" height="2980" fill="#fff"/>
  <polygon points="0,600 1200,600 1200,1000 0,760" fill="var(--beige)"/>
  <polygon points="0,1000 1200,1300 1200,2020 0,2020" fill="var(--beige)"/>
  <polygon points="0,1500 600,2020 0,2020" fill="var(--beige-deep)" opacity=".5"/>
  <polygon points="0,2240 1200,2240 1200,2300 0,2300" fill="var(--beige)"/>
  <rect x="0" y="3520" width="1200" height="480" fill="#fff"/>
  <rect x="0" y="4000" width="1200" height="240" fill="var(--beige)"/>
</svg>

<header>
  <div class="abs hero" role="img" aria-label="水色の柔らかな光のぼかし背景"></div>
  <nav class="abs gnav">
    <ul>
      <li>お知らせ</li><li>ごあいさつ</li><li>診療案内</li><li>乳がん検診</li><li>施設案内</li>
      <li>アクセスマップ</li><li>よくある質問</li><li>リンク</li>
      <li class="reserve">ご予約</li>
    </ul>
  </nav>
  <div class="abs brand">
    <div class="brand-name">ゆるね乳腺クリニック</div>
    <div class="brand-en">Yurune Breast Clinic</div>
  </div>
</header>

<section>
  <h2 class="abs news-label">お知らせ</h2>
  <ul class="abs news">
    <li><time>2024年00月00日</time>テキストが入ります。テキストが入ります。テキストが入ります。</li>
    <li><time>2024年00月00日</time>テキストが入ります。テキストが入ります。テキストが入ります。</li>
    <li><time>2024年00月00日</time>テキストが入ります。テキストが入ります。テキストが入ります。</li>
    <li><time>2024年00月00日</time>テキストが入ります。テキストが入ります。テキストが入ります。</li>
    <li><time>2024年00月00日</time>テキストが入ります。テキストが入ります。テキストが入ります。</li>
  </ul>
  <a class="abs news-more" href="#">お知らせ一覧はこちら ›</a>
</section>

<section class="abs card">
  <h2 class="abs sec-title" style="left:0;top:44px;width:880px">ごあいさつ</h2>
  <div class="abs doctor" role="img" aria-label="白衣の院長の写真"></div>
  <p class="abs doctor-cap">ゆるね乳腺クリニック 院長・医学博士</p>
  <div class="abs profile">
    <h4>【経歴】</h4>
    <p>平成元年 医科大学卒業。同大学附属病院外科に入局。<br>乳腺外科にて研修ののち総合病院乳腺科医長を歴任。<br>平成二十年 当院を開院し現在に至る。</p>
    <h4>【資格】</h4>
    <p>医学博士／南海外科医会 認定医<br>南海乳腺研究会 専門医<br>乳房画像読影 認定医</p>
  </div>
  <div class="abs greet-btn"><span class="sub-label">院長あいさつ</span></div>
  <p class="abs greet-text">当院のホームページをご覧いただきありがとうございます。乳がんは早期に発見し適切な治療を受けることで、多くの方が健やかな日常を取り戻せる病気です。当院では最新の検査機器をそろえ、女性の皆さまが安心して受診できるよう、ていねいな説明と落ち着いた環境づくりを心がけております。気になる症状がございましたら、どうぞお気軽にご相談ください。地域の皆さまの健康を支えるクリニックとして、スタッフ一同心よりお待ちしております。</p>
</section>

<section>
  <h2 class="abs sec-title" style="left:0;top:1590px;width:1200px">診療案内</h2>
  <span class="abs sub-label hours-label">診療時間</span>
  <table class="abs hours">
    <thead><tr><th></th><th>月</th><th>火</th><th>水</th><th>木</th><th>金</th><th>土</th></tr></thead>
    <tbody>
      <tr><td>午前 9:00〜12:30</td><td>○</td><td>○</td><td>○</td><td>○</td><td>○</td><td>○</td></tr>
      <tr><td>午後 14:00〜18:00</td><td>○</td><td>○</td><td>休</td><td>○</td><td>○</td><td>休</td></tr>
    </tbody>
  </table>
  <p class="abs hours-note">※受付は診療終了の30分前までとなります。<br>休診日：日曜・祝日・水曜午後・土曜午後</p>
  <span class="abs sub-label menu-label">診療内容</span>
  <div class="abs menus">
    <div class="menu">乳がん検診</div>
    <div class="menu">乳腺の超音波<br>（エコー）検査</div>
    <div class="menu">乳房の<br>しこり・痛みの<br>ご相談</div>
    <div class="menu">マンモ<br>グラフィ</div>
  </div>
  <a class="abs btn menu-btn" href="#">くわしい「診療内容」はこちら</a>
</section>

<section class="abs screen">
  <h2 class="abs sec-title" style="left:0;top:24px;width:1200px">乳がん検診（予約）</h2>
  <p class="abs screen-text">乳がん検診はマンモグラフィと超音波検査を組み合わせて行います。ご希望の日時をお電話にてご予約ください。<br>市町村の検診にも対応しております。受診票をお持ちのうえ、当日受付へお出しください。</p>
  <div class="abs screen-btn"><a class="btn" href="#">くわしい「乳がん検診（予約）」はこちら</a></div>
</section>

<section class="abs facility">
  <h2 class="abs sec-title" style="left:0;top:44px;width:1200px">施設案内</h2>
  <div class="abs fac-main" role="img" aria-label="白い外壁のクリニック外観写真"></div>
  <p class="abs fac-cap">施設案内のクリニック</p>
  <div class="abs thumbs">
    <div role="img" aria-label="受付の写真"></div>
    <div role="img" aria-label="待合室の写真"></div>
    <div role="img" aria-label="診察室の写真"></div>
    <div role="img" aria-label="検査室の写真"></div>
    <div role="img" aria-label="廊下の写真"></div>
    <div role="img" aria-label="処置室の写真"></div>
    <div role="img" aria-label="更衣室の写真"></div>
    <div role="img" aria-label="医療機器の写真"></div>
  </div>
</section>

<section>
  <h2 class="abs sec-title" style="left:0;top:3000px;width:1200px">よくある質問</h2>
  <ul class="abs faq">
    <li><span class="q">Q</span>乳房が痛む場合は受診すべきですか？<span class="chev">⌄</span></li>
    <li><span class="q">Q</span>検査は、乳房の一部分だけ行うのではなく、全体を調べていただけますか？<span class="chev">⌄</span></li>
    <li><span class="q">Q</span>乳房にしこりがあるのですが、どうすればよいですか？<span class="chev">⌄</span></li>
    <li><span class="q">Q</span>かならず紹介状がないと受診できないのでしょうか？<span class="chev">⌄</span></li>
    <li><span class="q">Q</span>しこりは良性か悪性か見分けられますか？<span class="chev">⌄</span></li>
    <li><span class="q">Q</span>検査当日の服装で気をつけることはありますか？<span class="chev">⌄</span></li>
    <li><span class="q">Q</span>検査の結果はいつ頃わかりますか？<span class="chev">⌄</span></li>
    <li><span class="q">Q</span>妊娠中や授乳中でも検査を受けられますか？<span class="chev">⌄</span></li>
    <li><span class="q">Q</span>乳房の検査は何年おきに受ければよいですか？<span class="chev">⌄</span></li>
  </ul>
  <div class="abs faq-btn"><a class="btn" href="#">「よくある質問」を表示する</a></div>
</section>

<section>
  <h2 class="abs sec-title" style="left:0;top:3530px;width:1200px">アクセスマップ</h2>
  <div class="abs acc-name">ゆるね乳腺クリニック</div>
  <p class="abs acc-addr">〒900-0000<br>沖縄県那覇市ゆるね町1-2-3</p>
  <a class="abs acc-tel" href="tel:0987654310">
    <svg width="30" height="30" viewBox="0 0 24 24" aria-hidden="true"><path fill="var(--navy)" d="M6.6 10.8a15.1 15.1 0 0 0 6.6 6.6l2.2-2.2c.3-.3.7-.4 1-.2 1.1.4 2.3.6 3.6.6.6 0 1 .4 1 1V20c0 .6-.4 1-1 1A17 17 0 0 1 3 4c0-.6.4-1 1-1h3.5c.6 0 1 .4 1 1 0 1.3.2 2.5.6 3.6.1.3 0 .7-.2 1z"/></svg>
    098-765-4310
  </a>
  <div class="abs map" role="img" aria-label="クリニック周辺の地図"></div>
</section>

<section>
  <h2 class="abs sec-title" style="left:0;top:4010px;width:1200px;font-size:18px">リンク</h2>
  <div class="abs links">
    <div><a href="#">南海乳腺研究会</a><br><a href="#">乳腺エコー研究会</a><br><a href="#">みなみ医師の会</a></div>
    <div><a href="#">乳房検診推進会</a><br><a href="#">女性がん相談室</a><br><a href="#">市民健康課</a></div>
    <div><a href="#">乳房画像診断研究会</a><br><a href="#">みなみ総合病院</a><br><a href="#">女性の健康ネット</a></div>
    <div><a href="#">乳腺クリニック会</a><br><a href="#">乳房ケア推進運動</a><br><a href="#">みなみ健康づくり財団</a></div>
  </div>
  <footer class="abs footer">Copyright © Yurune Breast Clinic. All Rights Reserved.</footer>
</section>

</body>
</html>
```